Design a upcoming mobile game webpage

I have a domain space up but as I am still needed to work on getting the content and every other things setup, I would like to at least populate the page with a coming soon page with videos/images or links to plenvo,qk etc and a newsletter sign up.
It can be design as a full game site but to illustrate it as "Coming soon to you on ZUL and Velmora"
Target Market(s)
Consumer who holds a mobile device
Industry/Entity Type
Velmora

```html
<!DOCTYPE html>
<html lang="en">
<head>
<meta charset="utf-8">
<title>Fabled Ascent — Launching Soon</title>
<link rel="stylesheet" href="https://fonts.googleapis.com/css2?family=Raleway:wght@300;400&family=Lato:wght@400;700&display=swap">
<style>
  :root {
    --navy: #06183a;
    --deep: #0b3a78;
    --accent: #3aaee0;
    --white: #ffffff;
    --title: #d9d9d9;
    --ink: #333333;
    --muted: #8a8a8a;
    --green: #5cbf87;
    --red: #e8535a;
  }
  * { box-sizing: border-box; margin: 0; padding: 0; }
  html, body { width: 957px; height: 1200px; overflow: hidden; background: var(--white); }
  .page { position: relative; width: 957px; height: 1200px; overflow: hidden; }

  .hero {
    position: absolute; left: 0; top: 0; width: 957px; height: 852px;
    background:
      radial-gradient(ellipse 520px 340px at 720px 620px, rgba(120,200,255,.55), rgba(120,200,255,0) 70%),
      radial-gradient(ellipse 700px 500px at 600px 450px, #1f6fbf, rgba(31,111,191,0) 75%),
      linear-gradient(180deg, var(--navy) 0%, var(--deep) 55%, #0d4f95 100%);
    border-bottom: 2px solid var(--accent);
  }
  .brand {
    position: absolute; left: 0; top: 40px; width: 957px; text-align: center;
    font-family: "Raleway", sans-serif; font-weight: 300; font-size: 66px; line-height: 76px;
    letter-spacing: 6px; color: var(--title); text-transform: uppercase;
  }

  .headline {
    position: absolute; left: 78px; top: 154px;
    font-family: "Raleway", sans-serif; font-weight: 400; font-size: 54px; line-height: 60px;
    color: var(--white); text-transform: uppercase;
  }
  .platforms {
    position: absolute; left: 78px; top: 354px;
    font-family: "Raleway", sans-serif; font-size: 46px; color: var(--white);
  }

  .device-art {
    position: absolute; left: 536px; top: 158px; width: 336px; height: 284px;
    border-radius: 22px;
    background: linear-gradient(135deg, #1a1a1a 0%, #3b3b3b 40%, #9fb4c8 55%, #1c1c1c 100%);
  }
  .store-names {
    position: absolute; left: 632px; top: 476px; display: flex; gap: 22px;
    font-family: "Lato", sans-serif; font-weight: 700; font-size: 20px; line-height: 28px; color: var(--white);
  }

  .subscribe { position: absolute; left: 80px; top: 470px; width: 355px; height: 42px; display: flex; }
  .subscribe .field {
    flex: 1; background: var(--white); border-radius: 4px 0 0 4px;
    font-family: "Lato", sans-serif; font-size: 12px; color: #999; line-height: 42px; padding-left: 10px;
  }
  .subscribe .button {
    width: 98px; background: var(--accent); border-radius: 0 4px 4px 0;
    font-family: "Lato", sans-serif; font-size: 14px; color: var(--white); line-height: 42px; text-align: center;
  }
  .note {
    position: absolute; left: 78px; top: 533px;
    font-family: "Lato", sans-serif; font-size: 20px; line-height: 24px; color: var(--white);
  }

  .countdown .unit {
    position: absolute; top: 612px; width: 168px; height: 168px; border-radius: 50%;
    background: var(--white); border: 3px solid var(--accent);
    font-family: "Lato", sans-serif; font-weight: 700; color: var(--accent); text-align: center;
  }
  .countdown .num { display: block; margin-top: 28px; font-size: 48px; line-height: 52px; }
  .countdown .label { display: block; font-size: 35px; line-height: 40px; }

  .social { position: absolute; left: 0; top: 808px; width: 957px; display: flex; justify-content: center; gap: 8px; }
  .social span {
    font-family: "Lato", sans-serif; font-size: 10px; color: var(--white);
    background: #2b5ea8; border-radius: 2px; padding: 2px 4px; line-height: 12px;
  }

  .features-title {
    position: absolute; left: 0; top: 896px; width: 957px; text-align: center;
    font-family: "Raleway", sans-serif; font-weight: 300; font-size: 29px; color: var(--ink);
  }
  .features-rule { position: absolute; left: 422px; top: 948px; width: 112px; height: 1px; background: var(--accent); }

  .feature { position: absolute; left: 80px; width: 350px; height: 80px; }
  .feature .mark { position: absolute; left: 0; top: 2px; width: 76px; height: 70px; border-radius: 6px; }
  .feature-chat .mark { background: var(--green); }
  .feature-basket .mark { background: var(--red); }
  .feature h3 {
    position: absolute; left: 108px; top: 0;
    font-family: "Raleway", sans-serif; font-weight: 400; font-size: 21px; color: #555;
  }
  .feature p {
    position: absolute; left: 109px; top: 30px; width: 240px;
    font-family: "Raleway", sans-serif; font-size: 12px; line-height: 24px; color: var(--muted); text-align: justify;
  }
  .feature-chat { top: 994px; }
  .feature-basket { top: 1094px; }

  .video-panel {
    position: absolute; left: 478px; top: 998px; width: 398px; height: 210px;
    border-radius: 16px 16px 0 0;
    background: linear-gradient(160deg, #6a5a4a 0%, #3a2e24 45%, #1d1a16 100%);
  }
</style>
</head>
<body>
<div class="page">
  <section class="hero">
    <h1 class="brand">Fabled Ascent</h1>
    <p class="headline">We are<br>launching<br>soon.....</p>
    <p class="platforms">“ZUL and Velmora”</p>

    <div class="device-art" role="img" aria-label="Three smartphones showing the game app screens"></div>
    <div class="store-names"><span>ZUL</span><span>Velmora</span></div>

    <div class="subscribe">
      <span class="field">Enter your Email to subscribe</span>
      <span class="button">Subscribe</span>
    </div>
    <p class="note">We'll be here soon with a new website.<br>Estimated Time Remaining.</p>

    <div class="countdown">
      <div class="unit" style="left:83px"><span class="num">45</span><span class="label">Days</span></div>
      <div class="unit" style="left:291px"><span class="num">15</span><span class="label">Hours</span></div>
      <div class="unit" style="left:499px"><span class="num">27</span><span class="label">Minutes</span></div>
      <div class="unit" style="left:707px"><span class="num">32</span><span class="label">Seconds</span></div>
    </div>

    <nav class="social">
      <span>qk</span><span>plenvo</span><span>Vidlo</span><span>Linkora</span>
    </nav>
  </section>

  <h2 class="features-title">FEATURES</h2>
  <div class="features-rule"></div>

  <div class="feature feature-chat">
    <div class="mark" role="img" aria-label="Messaging feature icon"></div>
    <h3>lorem ipsum</h3>
    <p>Lorem Ipsum is simply dummy text of the printing and typesetting industry.</p>
  </div>

  <div class="feature feature-basket">
    <div class="mark" role="img" aria-label="Shop feature icon"></div>
    <h3>lorem ipsum</h3>
    <p>Lorem Ipsum is simply dummy text of the printing and typesetting industry.</p>
  </div>

  <div class="video-panel" role="img" aria-label="Tablet playing the game trailer video"></div>
</div>
</body>
</html>
```